vantro - business cards

Need business card designs - logo provided - see www.vantro.co.nz

Industry/Entity Type

Business

Requirements
Must have
• logo - provided in attachments
• www.vantro.co.nz

```html
<!DOCTYPE html>
<html lang="en">
<head>
<meta charset="utf-8">
<title>vantro – business cards</title>
<link rel="stylesheet" href="https://fonts.googleapis.com/css2?family=Questrial&family=Arimo:wght@400;700&display=swap">
<style>
  :root {
    --bg: #d9d6d1;
    --card-light: #e8e8e8;
    --card-dark: #333333;
    --ink: #3a3a3a;
    --accent-blue: #1f7fc1;
    --accent-orange: #e87722;
    --text-light: #e4e4e4;
    --text-muted: #c9c9c9;
  }
  * { margin: 0; padding: 0; box-sizing: border-box; }
  html, body { width: 1200px; height: 900px; overflow: hidden; background: var(--bg); }
  .stage { position: relative; width: 1200px; height: 900px; }
  .card {
    position: absolute; left: 260px; width: 680px; height: 388px;
    background: var(--card-light); overflow: hidden;
    box-shadow: 0 4px 14px rgba(0,0,0,0.18);
    font-family: 'Arimo', Arial, sans-serif;
  }
  .card--front { top: 42px; }
  .card--back { top: 470px; }

  .brand { display: flex; align-items: center; gap: 14px; }
  .brand__dot { width: 54px; height: 54px; border-radius: 50%; background: var(--accent-blue); }
  .brand__name { font-family: 'Questrial', 'Century Gothic', sans-serif; color: var(--ink); font-size: 86px; line-height: 1; letter-spacing: 1px; }

  .card--front .brand { position: absolute; left: 50%; top: 150px; transform: translate(-50%, -50%); }
  .front__band { position: absolute; left: 0; bottom: 0; width: 100%; height: 88px; background: var(--card-dark); }
  .web { font-size: 17px; color: #fff; letter-spacing: 0.5px; }
  .web b { color: var(--accent-orange); font-weight: 700; }
  .front__web { position: absolute; left: 400px; top: 24px; padding-bottom: 8px; border-bottom: 3px solid var(--accent-orange); }

  .card--back .brand { position: absolute; left: 42px; top: 40px; }
  .card--back .brand__dot { width: 46px; height: 46px; }
  .card--back .brand__name { font-size: 72px; }
  .back__panel { position: absolute; left: 0; top: 150px; width: 100%; height: 238px; background: var(--card-dark); padding: 18px 42px; }
  .person { color: var(--text-light); font-size: 30px; margin-bottom: 12px; }
  .person__role { font-size: 13px; letter-spacing: 1px; color: var(--text-muted); margin-left: 8px; vertical-align: 6px; }
  .contacts { list-style: none; }
  .contacts li { color: var(--text-light); font-size: 16px; line-height: 24px; padding-left: 20px; position: relative; }
  .contacts li::before {
    content: ""; position: absolute; left: 2px; top: 8px;
    border-left: 8px solid var(--accent-orange); border-top: 5px solid transparent; border-bottom: 5px solid transparent;
  }
  .contacts strong { font-weight: 700; }
  .back__web { margin-top: 10px; padding-top: 8px; border-top: 3px solid var(--accent-orange); display: inline-block; margin-left: 20px; }
</style>
</head>
<body>
<main class="stage">
  <section class="card card--front" aria-label="Business card front">
    <div class="brand">
      <span class="brand__dot"></span>
      <span class="brand__name">vantro</span>
    </div>
    <div class="front__band">
      <p class="web front__web">www.<b>vantro</b>.co.nz</p>
    </div>
  </section>

  <section class="card card--back" aria-label="Business card back">
    <div class="brand">
      <span class="brand__dot"></span>
      <span class="brand__name">vantro</span>
    </div>
    <div class="back__panel">
      <p class="person">Miriam Calloway<span class="person__role">OPERATION MANAGER</span></p>
      <ul class="contacts">
        <li><strong>International:</strong> +64 21 480 936</li>
        <li><strong>Phone NZ:</strong> 0800 2 VANTRO (0800 82-68-76)</li>
        <li><strong>Email:</strong> info@vantro.co.nz</li>
        <li>P.O.Box 418207, Auckland, 0631, New Zealand</li>
      </ul>
      <p class="web back__web">www.<b>vantro</b>.co.nz</p>
    </div>
  </section>
</main>
</body>
</html>
```